IT Network Consultancy - Business Card

t4 linkways is a IT network consultancy based in London. We're looking for a smart, modern and professional business card design. Our website is here: www.t4linkways.co.uk

Key things that should be included on the card (with examples):

Company Logo
Name
Position / Job Title: Network Consultant
Mobile Phone Number: +44 (0) 7700 900418
Land Line: +44 (0) 1632 960274
Email Address: name@t4linkways.co.uk
Web Site URL: www.t4linkways.co.uk

Target Market(s)

Large enterprise / global companies / corporates

Industry/Entity Type

Business

Requirements
Must have
• Incorporate our logo - which is attached to the project. They are in AI format (can be opened in Inkscape).

The design should be double sided and fit on a UK standard 85mm × 55mm card and be in a format that retains the quality when printed.
Nice to have
• The project does not have to conform to the colour of our website but this should give you inspiration of the style we like.
Should not have
• Bright colours. Pictures are not necessary.

```html
<!DOCTYPE html>
<html lang="en">
<head>
<meta charset="utf-8">
<title>t4 linkways – Business Card</title>
<link rel="stylesheet" href="https://fonts.googleapis.com/css2?family=Questrial&family=Noto+Serif:ital,wght@0,400;0,700;1,400&display=swap">
<style>
  :root {
    --backdrop: #e4e2de;
    --card-dark: #2b2d30;
    --card-mid: #3b3e42;
    --card-light: #4a4d52;
    --logo-grey: #b8bcc1;
    --text-white: #f2f4f5;
    --text-mint: #b9e3d6;
    --map-tone-a: #3a3d40;
    --map-tone-b: #25272a;
    --divider: #5a5e63;
  }
  * { box-sizing: border-box; margin: 0; padding: 0; }
  html, body {
    width: 1200px;
    height: 900px;
    overflow: hidden;
    background: var(--backdrop);
  }
  .sheet {
    width: 1200px;
    height: 900px;
    display: flex;
    flex-direction: column;
    align-items: center;
    justify-content: center;
    gap: 40px;
  }
  .card {
    position: relative;
    width: 600px;
    height: 388px;
    border-radius: 22px;
    overflow: hidden;
    box-shadow: 0 6px 18px rgba(0, 0, 0, 0.25);
  }

  /* Front side */
  .card-front {
    background: var(--card-dark);
  }
  .front-backdrop {
    position: absolute;
    inset: 0;
    background: linear-gradient(160deg, var(--card-light) 0%, var(--card-mid) 45%, var(--card-dark) 100%);
  }
  .front-brand {
    position: absolute;
    left: 0;
    right: 0;
    top: 112px;
    text-align: center;
    font-family: "Questrial", sans-serif;
  }
  .front-brand .brand-name {
    font-size: 76px;
    letter-spacing: 1px;
    color: var(--logo-grey);
    line-height: 1;
  }
  .front-brand .brand-url {
    margin-top: 22px;
    font-size: 20px;
    letter-spacing: 1.5px;
    color: var(--text-white);
  }

  /* Back side */
  .card-back {
    background: var(--card-dark);
    font-family: "Noto Serif", serif;
    color: var(--text-mint);
  }
  .world-map {
    position: absolute;
    inset: 0;
    background: radial-gradient(ellipse at 45% 55%, var(--map-tone-a) 0%, var(--map-tone-b) 75%);
  }
  .back-brand {
    position: absolute;
    top: 30px;
    left: 0;
    right: 0;
    text-align: center;
    font-family: "Questrial", sans-serif;
    font-size: 38px;
    color: var(--text-white);
    letter-spacing: 1px;
  }
  .contact {
    position: absolute;
    left: 24px;
    top: 108px;
    width: 300px;
    text-align: center;
  }
  .contact .person-name {
    font-weight: 700;
    font-size: 24px;
  }
  .contact .job-title {
    font-style: italic;
    font-size: 15px;
    margin-bottom: 22px;
  }
  .contact .phone {
    font-size: 15px;
    line-height: 1.35;
  }
  .contact .email {
    margin-top: 24px;
    font-size: 15px;
  }
  .column-divider {
    position: absolute;
    left: 340px;
    top: 110px;
    width: 2px;
    height: 240px;
    background: var(--divider);
  }
  .services {
    position: absolute;
    left: 360px;
    right: 24px;
    top: 108px;
    text-align: center;
    font-size: 16px;
    line-height: 1.4;
    font-weight: 700;
  }
  .services .services-title {
    margin-bottom: 26px;
  }
</style>
</head>
<body>
<main class="sheet">

  <section class="card card-front" aria-label="Business card front">
    <div class="front-backdrop" role="img" aria-label="Soft grey gradient with faint curved background pattern"></div>
    <div class="front-brand">
      <div class="brand-name">t4 linkways</div>
      <div class="brand-url">www.t4linkways.co.uk</div>
    </div>
  </section>

  <section class="card card-back" aria-label="Business card back">
    <div class="world-map" role="img" aria-label="Faint world map with grid lines as card background"></div>
    <div class="back-brand">t4 linkways</div>

    <div class="contact">
      <div class="person-name">Name</div>
      <div class="job-title">Network Consultant</div>
      <div class="phone">+44 (0) 7700 900418</div>
      <div class="phone">+44 (0) 1632 960274</div>
      <div class="email">name@t4linkways.co.uk</div>
    </div>

    <div class="column-divider" aria-hidden="true"></div>

    <div class="services">
      <div class="services-title">We Offer</div>
      <div class="services-list">Architecture,<br>Design,<br>Implementation,<br>Network audit<br>and Team support<br>services.</div>
    </div>
  </section>

</main>
</body>
</html>
```